In Search of a FANTASTIC BUSINESS CARD REFRESH AND REDESIGN

I would like to redesign the current business card for my company.  There is a parent company, Brookfane Care Group, with 2 operating companies - Brookfane Homecare and Brookfane Senior Living.
I will include the current business card design, along with the 3 logos I would like incorporated.  The business card can be two sided.  I'm looking for something clean, professional, and a fresh new look.

Target Market(s)
Hospitals, social workers, insurance agents, family members of seniors
Industry/Entity Type
Healthcare
Contact Information for Business Card
Name, title of person, address, phone number, web address, email address
Look and feel
Each slider illustrates characteristics of the customer's brand and the style your logo design should communicate.

```html
<!DOCTYPE html>
<html lang="en">
<head>
<meta charset="utf-8">
<title>Brookfane Care Group – Business Card</title>
<link href="https://fonts.googleapis.com/css2?family=Roboto:wght@400;500;700&family=Lora:ital@1&display=swap" rel="stylesheet">
<style>
  :root {
    --backdrop: #3b3b3b;
    --card-white: #ffffff;
    --card-black: #141414;
    --coral: #f2706f;
    --teal: #3f8f8a;
    --ink: #4a4a4a;
    --ink-soft: #6b6b6b;
    --tagline: #e8e8e8;
  }
  * { box-sizing: border-box; margin: 0; padding: 0; }
  html, body { width: 1200px; height: 900px; overflow: hidden; }
  body {
    background: var(--backdrop);
    font-family: "Roboto", Arial, sans-serif;
    display: flex;
    align-items: center;
    justify-content: center;
    gap: 60px;
  }
  .card {
    position: relative;
    width: 520px;
    height: 297px;
    border-radius: 14px;
    overflow: hidden;
  }

  /* Front */
  .card--front { background: var(--card-white); color: var(--ink); }
  .brand-mark {
    display: flex;
    align-items: center;
    gap: 8px;
    font-family: "Roboto", Arial, sans-serif;
    font-weight: 700;
    white-space: nowrap;
  }
  .brand-mark__square { width: 22px; height: 22px; border-radius: 4px; flex: none; }
  .brand-mark--homecare { position: absolute; left: 34px; top: 34px; color: var(--coral); font-size: 18px; }
  .brand-mark--homecare .brand-mark__square { background: var(--coral); }
  .brand-mark--senior { position: absolute; right: 70px; bottom: 40px; color: var(--teal); font-size: 16px; }
  .brand-mark--senior .brand-mark__square { background: var(--teal); }

  .contact { position: absolute; left: 34px; top: 82px; font-size: 11.5px; line-height: 1.55; color: var(--ink-soft); list-style: none; }
  .contact__address { margin-bottom: 4px; }
  .contact li { display: flex; align-items: center; gap: 6px; }
  .contact svg { width: 10px; height: 10px; flex: none; }

  .holder { position: absolute; right: 46px; top: 96px; text-align: right; }
  .holder__name { font-size: 21px; font-weight: 700; letter-spacing: 0.5px; text-transform: uppercase; white-space: nowrap; }
  .holder__first { color: var(--teal); }
  .holder__last { color: var(--coral); }
  .holder__title { font-size: 13px; color: var(--ink-soft); margin-top: 2px; }

  .edge-tab { position: absolute; right: 0; top: 0; width: 16px; height: 44px; background: var(--teal); }

  /* Back */
  .card--back { background: var(--card-black); color: var(--card-white); display: flex; flex-direction: column; align-items: center; justify-content: center; gap: 16px; }
  .brand-mark--group { color: var(--card-white); font-size: 28px; gap: 12px; }
  .brand-mark--group .brand-mark__square { background: var(--card-white); width: 30px; height: 30px; }
  .tagline { font-family: "Lora", Georgia, serif; font-style: italic; font-size: 13px; text-align: center; line-height: 1.5; color: var(--tagline); }
</style>
</head>
<body>
  <section class="card card--front" aria-label="Card front">
    <div class="edge-tab"></div>
    <div class="brand-mark brand-mark--homecare"><span class="brand-mark__square"></span>Brookfane Homecare</div>

    <ul class="contact">
      <li class="contact__address">415 Harborview Ave, Suite<br>210, Lanford, HI 96720</li>
      <li><svg viewBox="0 0 10 10"><path d="M2 1h2l1 2-1.2 1a5 5 0 0 0 2.2 2.2L7 5l2 1v2a1 1 0 0 1-1 1A7 7 0 0 1 1 2a1 1 0 0 1 1-1z" fill="var(--teal)"/></svg>(555) 014-2286</li>
      <li><svg viewBox="0 0 10 10"><rect x="1.5" y="1" width="7" height="3" fill="none" stroke="var(--teal)"/><rect x="0.5" y="4" width="9" height="5" rx="1" fill="var(--teal)"/></svg>(555) 014-2290</li>
      <li><svg viewBox="0 0 10 10"><rect x="0.5" y="2" width="9" height="6" fill="none" stroke="var(--teal)"/><path d="M0.5 2l4.5 3.5L9.5 2" fill="none" stroke="var(--teal)"/></svg>marla@brookfanecare.com</li>
      <li><svg viewBox="0 0 10 10"><circle cx="5" cy="5" r="4.5" fill="var(--teal)"/><path d="M0.5 5h9M5 0.5c-2 2.5-2 6.5 0 9M5 0.5c2 2.5 2 6.5 0 9" fill="none" stroke="#fff" stroke-width="0.6"/></svg>www.brookfanecare.com</li>
    </ul>

    <div class="holder">
      <p class="holder__name"><span class="holder__first">Marla</span> <span class="holder__last">Denholt</span></p>
      <p class="holder__title">President, CEO</p>
    </div>

    <div class="brand-mark brand-mark--senior"><span class="brand-mark__square"></span>Brookfane Senior Living</div>
  </section>

  <section class="card card--back" aria-label="Card back">
    <div class="brand-mark brand-mark--group"><span class="brand-mark__square"></span>Brookfane Care Group</div>
    <p class="tagline">Close by when it matters...<br>Every single day.</p>
  </section>
</body>
</html>
```